Now Leasing Banner

Looking for a banner that says the following information approx 4' x 30'

Now Leasing Maple Ridge Court 925-318-6042

Target Market(s)

Drive by traffic

Industry/Entity Type

Residential property management

Requirements
Must have
• Clear and readable from a distance

```html
<!DOCTYPE html>
<html lang="en">
<head>
<meta charset="utf-8">
<title>Now Leasing Banner – Maple Ridge Court</title>
<link href="https://fonts.googleapis.com/css2?family=Oswald:wght@700&family=Encode+Sans+Semi+Condensed:wght@700;800&display=swap" rel="stylesheet">
<style>
  :root {
    --page-bg: #f2f2f2;
    --banner-bg: #ffffff;
    --navy: #1f3064;
    --red: #e63b35;
    --white: #ffffff;
    --photo-light: #efe2da;
    --photo-mid: #c9a48e;
    --photo-dark: #6b4a3a;
  }
  * { margin: 0; padding: 0; box-sizing: border-box; }
  html, body {
    width: 1200px;
    height: 1108px;
    overflow: hidden;
    background: var(--page-bg);
  }
  .canvas {
    position: relative;
    width: 1200px;
    height: 1108px;
  }
  .banner {
    position: absolute;
    left: 30px;
    top: 471px;
    width: 1140px;
    height: 166px;
    background: var(--banner-bg);
    box-shadow: 0 2px 8px rgba(0, 0, 0, 0.15);
    overflow: hidden;
  }
  .agent-photo {
    position: absolute;
    left: 6px;
    top: 10px;
    width: 160px;
    height: 156px;
    background: radial-gradient(ellipse at 40% 35%, var(--photo-light) 0%, var(--photo-mid) 55%, var(--photo-dark) 100%);
    border-radius: 6px 6px 0 0;
  }
  .headline {
    position: absolute;
    left: 199px;
    top: 34px;
    width: 455px;
    font-family: "Oswald", "Arial Narrow", sans-serif;
    font-weight: 700;
    font-size: 82px;
    line-height: 1;
    color: var(--red);
    text-shadow: 3px 3px 0 var(--navy);
    white-space: nowrap;
  }
  .property-name {
    position: absolute;
    left: 666px;
    top: 16px;
    width: 474px;
    font-family: "Encode Sans Semi Condensed", "Arial Narrow", sans-serif;
    font-weight: 800;
    font-size: 48px;
    line-height: 1.1;
    color: var(--navy);
    white-space: nowrap;
    text-align: center;
  }
  .phone-band {
    position: absolute;
    left: 666px;
    top: 87px;
    width: 474px;
    height: 79px;
    background: var(--navy);
    display: flex;
    align-items: center;
    justify-content: center;
  }
  .phone-number {
    font-family: "Encode Sans Semi Condensed", "Arial Narrow", sans-serif;
    font-weight: 700;
    font-size: 60px;
    line-height: 1;
    color: var(--white);
    white-space: nowrap;
  }
</style>
</head>
<body>
  <main class="canvas">
    <section class="banner">
      <div class="agent-photo" role="img" aria-label="Photo of a smiling leasing agent holding out a set of keys"></div>
      <h1 class="headline">NOW LEASING</h1>
      <h2 class="property-name">Maple Ridge Court</h2>
      <div class="phone-band">
        <p class="phone-number">925-318-6042</p>
      </div>
    </section>
  </main>
</body>
</html>
```